BRAVO (Bright Regional Applied Vector Operations) Letter Head Design Project

Company Name: BRAVO (Bright Regional Applied Vector Operations) MFZ.
Office Address: Office No 718, Saffron Crest Block, Palmera Garden Quarter, Dubai, U.A.E
Company line of business:
1) Currently we have a POS solution for retail outlets like duty free shops, supermarkets, department stores etc... The solution is deployed in Harbourline Travel Retail on 350 POS and in Corniche Gate Travel Retail on 100 POS. So our main line of business is the deployment of this solution in retail outlets locally or regionally. We have already deployed the solution in India and Australia.
2) Integration of other third party POS systems with an online credit authorization netwotk in the UAE. This will enable POS applications to connect directly to the acquiring banks without needing an EFT terminal like Paxomat or Tallyrex. The credit card payment is completed at the POS.
3) Other solutions that are targeting retail outlets like mobile POS, queue busting solutions, stock taking solutions using hand held devices, transaction capture systems, etc...
4) Other IT services like support of call center solutions from Bluegrove Systems and development of new solutions as per customer requirements.
We need a letter head design for the company. We don't have any specific requirements in mind and we prefer to leave it up to the designers to come up with creative designs that will not be limited by any guidelines.
Updates
I have just uploaded all the files I received from my company logo designer. Please review and let me know if you need anything else. .
Dear All,
I have received very nice designs and I thank you for all the hard work you have put so far. I would like the letter head to have all the following company details:
Office Address: Office No 718, Saffron Crest Block, MFZ, Dubai UAE
P.O.Box: 58316 Dubai UAE
Tel Number:+971-4-5817730
Fax Number::+971-4-5817731
Website:www.bravomfz.ae
I would also like to represent the company details as a QRCode somewhere on the page, probably next to the company details if possible (as a trial).
In case you have included a butterfly in the middle of the page as part of your design, I prefer that it doesn't include any colors as colors might make reading the text on the page more difficult.
I don't want to have too many butterflies on the page. 2 are more than enough.
Can you also include a design for the continuation pages?
Thank you in advance and I look forward to receiving your creative designs.
Regards
Samir Odeyra

```html
<!DOCTYPE html>
<html lang="en">
<head>
<meta charset="utf-8">
<title>BRAVO Letterhead</title>
<link rel="stylesheet" href="https://fonts.googleapis.com/css2?family=Carlito:wght@400;700&display=swap">
<style>
  :root {
    --paper: #ffffff;
    --ink: #1c1c1c;
    --muted: #555555;
    --brand-dot: #1f5fae;
    --watermark: #ececec;
    --watermark-dot: #f1f1f1;
    --code-fill: #d9d9d9;
    --green: #9cc32a;
    --blue: #1e8fd6;
    --purple: #5b3f93;
    --red: #e0262b;
  }
  * { margin: 0; padding: 0; box-sizing: border-box; }
  html, body {
    width: 848px;
    height: 1200px;
    overflow: hidden;
    background: var(--paper);
  }
  .letterhead {
    position: relative;
    width: 848px;
    height: 1200px;
    background: var(--paper);
    font-family: "Carlito", "Calibri", sans-serif;
    color: var(--ink);
  }
  .brand {
    position: absolute;
    left: 30px;
    top: 26px;
    display: flex;
    align-items: center;
    gap: 12px;
  }
  .brand-dot {
    width: 36px;
    height: 36px;
    border-radius: 50%;
    background: var(--brand-dot);
  }
  .brand-name {
    font-size: 40px;
    font-weight: 700;
    letter-spacing: 1px;
    line-height: 1;
    color: var(--ink);
  }
  .rule {
    position: absolute;
    height: 2px;
  }
  .rule-top {
    left: 8px;
    top: 94px;
    width: 682px;
    background: linear-gradient(to right, var(--green) 0%, var(--blue) 38%, var(--purple) 52%, var(--red) 68%, rgba(224,38,43,0) 100%);
  }
  .rule-bottom {
    left: 160px;
    top: 1142px;
    width: 680px;
    background: linear-gradient(to right, rgba(224,38,43,0) 0%, var(--red) 32%, var(--purple) 50%, var(--blue) 64%, var(--green) 100%);
  }
  .watermark {
    position: absolute;
    left: 220px;
    top: 540px;
    display: flex;
    align-items: center;
    gap: 24px;
  }
  .watermark-dot {
    width: 110px;
    height: 110px;
    border-radius: 50%;
    background: var(--watermark-dot);
  }
  .watermark-name {
    font-size: 96px;
    font-weight: 700;
    letter-spacing: 4px;
    line-height: 1;
    color: var(--watermark);
  }
  .company-code {
    position: absolute;
    left: 40px;
    top: 1120px;
    width: 60px;
    height: 60px;
  }
  .footer {
    position: absolute;
    left: 110px;
    right: 10px;
    top: 1150px;
    text-align: center;
    white-space: nowrap;
    line-height: 1.25;
  }
  .footer-address {
    font-size: 15px;
    color: var(--ink);
  }
  .footer-contact {
    font-size: 13px;
    color: var(--muted);
    margin-top: 3px;
  }
  .footer-contact .sep {
    padding: 0 6px;
    color: var(--red);
  }
</style>
</head>
<body>
  <div class="letterhead">
    <header class="brand">
      <span class="brand-dot"></span>
      <span class="brand-name">BRAVO</span>
    </header>
    <div class="rule rule-top"></div>

    <div class="watermark" aria-hidden="true">
      <span class="watermark-dot"></span>
      <span class="watermark-name">BRAVO</span>
    </div>

    <svg class="company-code" viewBox="0 0 60 60" role="img" aria-label="QR code holding the company contact details">
      <rect x="0" y="0" width="60" height="60" fill="var(--code-fill)"/>
    </svg>

    <div class="rule rule-bottom"></div>
    <footer class="footer">
      <p class="footer-address">Bright Regional Applied Vector Operations&nbsp; Office No 718, Saffron Crest Block, Palmera Garden Quarter, Dubai, U.A.E</p>
      <p class="footer-contact">P.O.Box: 58316 Dubai UAE<span class="sep">|</span>Tel: +971-4-5817730<span class="sep">|</span>Fax: +971-4-5817731<span class="sep">|</span>www.bravomfz.ae</p>
    </footer>
  </div>
</body>
</html>
```